Book Cover - For Best Selling Diet

Hi
Book cover required for a diet book being marketed to become a best seller
For best quality, image will be 2820 pixels on the shortest side and 4500 pixels on the longest side .
The book name : Bright Morning Plan
By Corinna Plett
( will add in the extra text once we see design - top and bottom subtitle )
I do not want a photo of a person on the book.
PLEASE SEE " THE 9 STEP FRAME" by Ned Galbury as an example of solid style and I also love Quiet Ledger for the font.
Branding Colours:
#F26432
#A4195C
#A7D8CC
Font that runs through our brand is : helvetica neue
This is for a book that will be marketed for #1 bestseller - So please only quality
designs that are designed in a unique style.
Thanks
Target Market(s)
Busy Working Mums, Affluent, 30+ .
Look and feel

```html
<!DOCTYPE html>
<html lang="en">
<head>
<meta charset="utf-8">
<title>Bright Morning Plan — Book Cover</title>
<link rel="stylesheet" href="https://fonts.googleapis.com/css2?family=Inter:wght@400&family=Josefin+Sans:wght@200;300&display=swap">
<style>
  :root {
    --berry: #A4195C;
    --tangerine: #F26432;
    --mint: #A7D8CC;
    --paper: #FFFFFF;
    --ink-light: #FFFFFF;
  }
  * { margin: 0; padding: 0; box-sizing: border-box; }
  html, body {
    width: 1200px;
    height: 1000px;
    overflow: hidden;
    background: var(--paper);
  }
  .stage {
    position: relative;
    width: 1200px;
    height: 1000px;
  }
  .book-cover {
    position: absolute;
    left: 411px;
    top: 210px;
    width: 378px;
    height: 600px;
    background: var(--berry);
    box-shadow: 2px 3px 6px rgba(0, 0, 0, 0.18);
    overflow: hidden;
  }
  .title {
    position: absolute;
    left: 0;
    top: 84px;
    width: 100%;
    text-align: center;
    font-family: "Josefin Sans", sans-serif;
    font-weight: 200;
    font-size: 60px;
    line-height: 77px;
    letter-spacing: 3px;
    color: var(--ink-light);
    text-transform: uppercase;
  }
  .title-line { display: block; }
  .title-line--accent { color: var(--mint); }
  .title-line--long { font-size: 52px; letter-spacing: 2px; }
  .author-band {
    position: absolute;
    left: 0;
    top: 357px;
    width: 100%;
    height: 49px;
    background: var(--mint);
  }
  .author-band__inner {
    position: absolute;
    left: 0;
    top: 5px;
    width: 100%;
    height: 38px;
    background: var(--tangerine);
    display: flex;
    align-items: center;
    justify-content: center;
    font-family: "Inter", sans-serif;
    font-weight: 400;
    color: var(--ink-light);
  }
  .author-band__by { font-size: 14px; margin-right: 6px; margin-top: 3px; }
  .author-band__name { font-size: 19px; letter-spacing: 0.2px; }
  .balance-illustration {
    position: absolute;
    left: 55px;
    top: 450px;
    width: 270px;
    height: 150px;
    background: linear-gradient(180deg, rgba(255,255,255,0.85) 0%, rgba(255,255,255,0.95) 100%);
    border-radius: 8px 8px 0 0;
  }
</style>
</head>
<body>
  <main class="stage">
    <section class="book-cover">
      <h1 class="title">
        <span class="title-line">Bright</span>
        <span class="title-line title-line--long">Morning</span>
        <span class="title-line title-line--accent">Plan</span>
      </h1>
      <div class="author-band">
        <p class="author-band__inner">
          <span class="author-band__by">By</span>
          <span class="author-band__name">Corinna Plett</span>
        </p>
      </div>
      <div class="balance-illustration" role="img" aria-label="White silhouette of a seesaw scale balancing an apple against a burger"></div>
    </section>
  </main>
</body>
</html>
```